Graphic design change project

The task is to take some existing images, and edit them so that they are simplified and white, with a transparent background (they will be used on a website with a black/dark background)

Attached are 10 images.

The first image (What the images should look like.PNG) shows the look and feel of what the images should look like.

The second image (overview of page design.jpg) shows how the images will be used on the website, along with the general look and feel of the website).

The other 9 images are the images that we would like edited to have the look and feel of the first image.

If successful, we will have more images that we will ask you to edit on an on-going basis. (for an additional fee).

```html
<!DOCTYPE html>
<html lang="en">
<head>
<meta charset="utf-8">
<title>Service Cycle</title>
<link rel="stylesheet" href="https://fonts.googleapis.com/css2?family=Source+Sans+3:wght@700&display=swap">
<style>
  :root {
    --page: #ffffff;
    --panel: #555555;
    --arrow: #fafafa;
    --arrow-soft: #f2f2f2;
    --label: #ffffff;
  }
  html, body {
    margin: 0;
    padding: 0;
    width: 873px;
    height: 1200px;
    overflow: hidden;
    background: var(--page);
  }
  .cycle-graphic {
    display: block;
    width: 873px;
    height: 1200px;
  }
  .cycle-panel { fill: var(--panel); }
  .loop-arc {
    fill: none;
    stroke: var(--arrow);
    stroke-width: 40;
    stroke-linecap: butt;
  }
  .loop-arc--final { stroke: var(--arrow-soft); }
  .loop-head { fill: var(--arrow); }
  .step-label {
    fill: var(--label);
    font-family: "Source Sans 3", "Myriad Pro", Arial, sans-serif;
    font-weight: 700;
    font-size: 36px;
    text-anchor: middle;
  }
</style>
</head>
<body>
<svg class="cycle-graphic" viewBox="0 0 800 1100" xmlns="http://www.w3.org/2000/svg" role="img" aria-label="Service cycle: Availability, SLA, Integration, Efficiency">
  <rect class="cycle-panel" x="175" y="62" width="449" height="975"/>

  <!-- Step 1: Availability -->
  <path class="loop-arc" d="M315 228 A140 140 0 1 1 491 363"/>
  <polygon class="loop-head" points="490,322 490,408 448,368"/>

  <!-- Step 2: SLA -->
  <path class="loop-arc" d="M464 354 A142 142 0 1 0 321 583"/>
  <polygon class="loop-head" points="320,530 320,620 360,577"/>

  <!-- Step 3: Integration -->
  <path class="loop-arc" d="M361 556 A140 140 0 1 1 489 792"/>
  <polygon class="loop-head" points="490,750 490,838 448,795"/>

  <!-- Step 4: Efficiency -->
  <path class="loop-arc loop-arc--final" d="M452 771 A140 140 0 1 0 493 870"/>

  <text class="step-label" x="457" y="243">Availability</text>
  <text class="step-label" x="352" y="458">SLA</text>
  <text class="step-label" x="456" y="672">Integration</text>
  <text class="step-label" x="351" y="887">Efficiency</text>
</svg>
</body>
</html>
```